We are looking to create a graphic that will be used in Facebook posts each week to show the daily Fernvale Bulletin. Attached is an example of what we are looking for. We need to be able to update the forecast. So we will need hi-res vector files. The graphics need to represent the level of mosquito activity: SLIGHT, AVERAGE, INTENSE, EXTREME

```html
<!DOCTYPE html>
<html lang="en">
<head>
<meta charset="utf-8">
<title>Fernvale Bulletin – Weekly Activity</title>
<link href="https://fonts.googleapis.com/css2?family=Open+Sans:wght@400;700&display=swap" rel="stylesheet">
<style>
  :root {
    --page: #ffffff;
    --pond-a: #5c9f86;
    --pond-b: #6fae8e;
    --pond-c: #86bf8c;
    --title: #262626;
    --card-top: #303030;
    --card-bottom: #000000;
    --card-text: #ffffff;
    --tick-dim: #454545;
    --level-slight: #3ddb35;
    --level-average: #f5e10c;
    --level-intense: #fb7a10;
    --level-extreme: #ec1b1a;
  }
  * { margin: 0; padding: 0; box-sizing: border-box; }
  html, body { width: 1200px; height: 1200px; overflow: hidden; background: var(--page); }
  body { position: relative; font-family: "Open Sans", Arial, sans-serif; }

  .bulletin {
    position: absolute;
    left: 54px; top: 214px;
    width: 1092px; height: 772px;
    overflow: hidden;
  }
  .bulletin__backdrop {
    position: absolute; inset: 0;
    background:
      radial-gradient(ellipse at 85% 80%, var(--pond-c) 0%, transparent 55%),
      radial-gradient(ellipse at 75% 20%, #8dc493 0%, transparent 45%),
      linear-gradient(135deg, var(--pond-a) 0%, var(--pond-b) 100%);
  }
  .bulletin__title {
    position: absolute;
    left: 78px; top: 314px;
    font-weight: 700;
    font-size: 67px;
    line-height: 1;
    letter-spacing: -0.5px;
    color: var(--title);
  }
  .forecast {
    position: absolute;
    left: 78px; top: 404px;
    display: flex;
    gap: 7.2px;
    list-style: none;
  }
  .day-card {
    width: 128px; height: 227px;
    border-radius: 16px;
    background: linear-gradient(180deg, var(--card-top) 0%, var(--card-bottom) 100%);
    color: var(--card-text);
    text-align: center;
    position: relative;
  }
  .day-card__date {
    position: absolute; top: 22px; left: 0; right: 0;
    font-size: 14px; line-height: 18px;
  }
  .day-card__gauge {
    position: absolute; left: 20px; top: 72px;
    width: 88px; height: 88px;
  }
  .day-card__level {
    position: absolute; top: 190px; left: 0; right: 0;
    font-size: 14.5px;
  }
</style>
</head>
<body>
<svg width="0" height="0" style="position:absolute" aria-hidden="true">
  <defs>
    <g id="ring-dim" stroke="var(--tick-dim)" stroke-width="4" stroke-linecap="round">
      <line y1="-27" y2="-42" transform="rotate(187.5)"/><line y1="-27" y2="-42" transform="rotate(202.5)"/>
      <line y1="-27" y2="-42" transform="rotate(217.5)"/><line y1="-27" y2="-42" transform="rotate(232.5)"/>
      <line y1="-27" y2="-42" transform="rotate(247.5)"/><line y1="-27" y2="-42" transform="rotate(262.5)"/>
      <line y1="-27" y2="-42" transform="rotate(277.5)"/><line y1="-27" y2="-42" transform="rotate(292.5)"/>
      <line y1="-27" y2="-42" transform="rotate(307.5)"/><line y1="-27" y2="-42" transform="rotate(322.5)"/>
      <line y1="-27" y2="-42" transform="rotate(337.5)"/><line y1="-27" y2="-42" transform="rotate(352.5)"/>
      <line y1="-27" y2="-42" transform="rotate(7.5)"/><line y1="-27" y2="-42" transform="rotate(22.5)"/>
      <line y1="-27" y2="-42" transform="rotate(37.5)"/><line y1="-27" y2="-42" transform="rotate(52.5)"/>
      <line y1="-27" y2="-42" transform="rotate(67.5)"/><line y1="-27" y2="-42" transform="rotate(82.5)"/>
      <line y1="-27" y2="-42" transform="rotate(97.5)"/><line y1="-27" y2="-42" transform="rotate(112.5)"/>
      <line y1="-27" y2="-42" transform="rotate(127.5)"/><line y1="-27" y2="-42" transform="rotate(142.5)"/>
      <line y1="-27" y2="-42" transform="rotate(157.5)"/><line y1="-27" y2="-42" transform="rotate(172.5)"/>
    </g>
    <g id="ring-lit" stroke-width="4" stroke-linecap="round">
      <line y1="-27" y2="-42" stroke="#1fcf5a" transform="rotate(187.5)"/><line y1="-27" y2="-42" stroke="#22d24f" transform="rotate(202.5)"/>
      <line y1="-27" y2="-42" stroke="#2bd642" transform="rotate(217.5)"/><line y1="-27" y2="-42" stroke="#3ddb35" transform="rotate(232.5)"/>
      <line y1="-27" y2="-42" stroke="#52df2a" transform="rotate(247.5)"/><line y1="-27" y2="-42" stroke="#6ee220" transform="rotate(262.5)"/>
      <line y1="-27" y2="-42" stroke="#8be41a" transform="rotate(277.5)"/><line y1="-27" y2="-42" stroke="#a8e616" transform="rotate(292.5)"/>
      <line y1="-27" y2="-42" stroke="#c6e712" transform="rotate(307.5)"/><line y1="-27" y2="-42" stroke="#e2e80f" transform="rotate(322.5)"/>
      <line y1="-27" y2="-42" stroke="#f5e10c" transform="rotate(337.5)"/><line y1="-27" y2="-42" stroke="#fbcb0b" transform="rotate(352.5)"/>
      <line y1="-27" y2="-42" stroke="#fdb30b" transform="rotate(7.5)"/><line y1="-27" y2="-42" stroke="#fd9a0c" transform="rotate(22.5)"/>
      <line y1="-27" y2="-42" stroke="#fc830e" transform="rotate(37.5)"/><line y1="-27" y2="-42" stroke="#fb6c10" transform="rotate(52.5)"/>
      <line y1="-27" y2="-42" stroke="#f95612" transform="rotate(67.5)"/><line y1="-27" y2="-42" stroke="#f74314" transform="rotate(82.5)"/>
      <line y1="-27" y2="-42" stroke="#f43316" transform="rotate(97.5)"/><line y1="-27" y2="-42" stroke="#f02618" transform="rotate(112.5)"/>
      <line y1="-27" y2="-42" stroke="#ec1b1a" transform="rotate(127.5)"/><line y1="-27" y2="-42" stroke="#e8141b" transform="rotate(142.5)"/>
      <line y1="-27" y2="-42" stroke="#e3101c" transform="rotate(157.5)"/><line y1="-27" y2="-42" stroke="#de0e1d" transform="rotate(172.5)"/>
    </g>
    <clipPath id="level-slight"><path d="M0 0 L0 50 A50 50 0 0 1 -48.3 -12.9 Z"/></clipPath>
    <clipPath id="level-average"><path d="M0 0 L0 50 A50 50 0 0 1 -12.9 -48.3 Z"/></clipPath>
    <clipPath id="level-intense"><path d="M0 0 L0 50 A50 50 0 1 1 48.3 -12.9 Z"/></clipPath>
  </defs>
</svg>

<section class="bulletin">
  <div class="bulletin__backdrop" role="img" aria-label="Soft photo of a pond with lotus leaves and a pink lotus bud"></div>
  <h1 class="bulletin__title">Fernvale Bulletin</h1>

  <ul class="forecast">
    <li class="day-card">
      <p class="day-card__date">Sun<br>2/19</p>
      <svg class="day-card__gauge" viewBox="-44 -44 88 88">
        <use href="#ring-dim"/><use href="#ring-lit" clip-path="url(#level-average)"/>
        <circle r="7" fill="var(--level-average)" role="img" aria-label="Mosquito icon"/>
      </svg>
      <p class="day-card__level">Average</p>
    </li>
    <li class="day-card">
      <p class="day-card__date">Mon<br>2/20</p>
      <svg class="day-card__gauge" viewBox="-44 -44 88 88">
        <use href="#ring-dim"/><use href="#ring-lit" clip-path="url(#level-intense)"/>
        <circle r="7" fill="var(--level-intense)" role="img" aria-label="Mosquito icon"/>
      </svg>
      <p class="day-card__level">Intense</p>
    </li>
    <li class="day-card">
      <p class="day-card__date">Tue<br>2/21</p>
      <svg class="day-card__gauge" viewBox="-44 -44 88 88">
        <use href="#ring-lit"/>
        <circle r="7" fill="var(--level-extreme)" role="img" aria-label="Mosquito icon"/>
      </svg>
      <p class="day-card__level">Extreme</p>
    </li>
    <li class="day-card">
      <p class="day-card__date">Wed<br>2/22</p>
      <svg class="day-card__gauge" viewBox="-44 -44 88 88">
        <use href="#ring-lit"/>
        <circle r="7" fill="var(--level-extreme)" role="img" aria-label="Mosquito icon"/>
      </svg>
      <p class="day-card__level">Extreme</p>
    </li>
    <li class="day-card">
      <p class="day-card__date">Thu<br>2/23</p>
      <svg class="day-card__gauge" viewBox="-44 -44 88 88">
        <use href="#ring-dim"/><use href="#ring-lit" clip-path="url(#level-intense)"/>
        <circle r="7" fill="var(--level-intense)" role="img" aria-label="Mosquito icon"/>
      </svg>
      <p class="day-card__level">Intense</p>
    </li>
    <li class="day-card">
      <p class="day-card__date">Fri<br>2/24</p>
      <svg class="day-card__gauge" viewBox="-44 -44 88 88">
        <use href="#ring-dim"/><use href="#ring-lit" clip-path="url(#level-average)"/>
        <circle r="7" fill="var(--level-average)" role="img" aria-label="Mosquito icon"/>
      </svg>
      <p class="day-card__level">Average</p>
    </li>
    <li class="day-card">
      <p class="day-card__date">Sat<br>2/25</p>
      <svg class="day-card__gauge" viewBox="-44 -44 88 88">
        <use href="#ring-dim"/><use href="#ring-lit" clip-path="url(#level-slight)"/>
        <circle r="7" fill="var(--level-slight)" role="img" aria-label="Mosquito icon"/>
      </svg>
      <p class="day-card__level">Slight</p>
    </li>
  </ul>
</section>
</body>
</html>
```